Stationary for IT communtications company
We send SMS and email messages to pet owners from veterinary practices
Stationary for IT communtications company - Information Technology
Creative Brief
Modern
Dominic Pelling MRCVS
Mr
Oakmere Stanhurst Lode Norwich NR14 2QJ
dominic@quietnudge.co.uk
www.quietnudge.co.uk
Quiet Nudge Logo

```html
<!DOCTYPE html>
<html lang="en">
<head>
<meta charset="utf-8">
<title>Quiet Nudge — Business Card</title>
<link rel="stylesheet" href="https://fonts.googleapis.com/css2?family=Michroma&display=swap">
<style>
  :root {
    --backdrop: #e9e7e3;
    --card: #ffffff;
    --ink: #3a3d40;
    --ink-soft: #6b6f73;
    --green: #5aa82a;
    --green-light: #8cc63f;
    --green-dark: #3f8a1c;
  }
  * { margin: 0; padding: 0; box-sizing: border-box; }
  html, body {
    width: 1200px; height: 629px; overflow: hidden;
    background: var(--backdrop);
    font-family: "Michroma", sans-serif;
    color: var(--ink);
  }
  .stage {
    width: 1200px; height: 629px;
    display: flex; align-items: center; justify-content: center; gap: 60px;
  }
  .card {
    position: relative;
    width: 520px; height: 300px;
    background: var(--card);
    box-shadow: 0 6px 18px rgba(0,0,0,0.12);
    overflow: hidden;
  }
  .brand { display: flex; align-items: center; gap: 14px; }
  .brand-dot {
    width: 44px; height: 44px; border-radius: 50%;
    background: var(--green);
  }
  .brand-name {
    font-size: 30px; letter-spacing: 2px; text-transform: uppercase;
    color: var(--ink); line-height: 1;
  }
  .card-front { display: flex; align-items: center; justify-content: center; }

  .card-back .brand { position: absolute; left: 34px; top: 40px; }
  .card-back .brand-dot { width: 34px; height: 34px; }
  .card-back .brand-name { font-size: 22px; }

  .holder {
    position: absolute; right: 40px; top: 118px;
    font-size: 10px; letter-spacing: 2px; text-transform: uppercase;
    color: var(--green);
  }
  .contact-list {
    position: absolute; right: 40px; top: 150px;
    list-style: none;
    display: flex; flex-direction: column; gap: 7px;
  }
  .contact-item {
    display: flex; align-items: center; gap: 8px;
    font-size: 8px; letter-spacing: 1px; color: var(--ink-soft);
  }
  .contact-icon {
    width: 12px; height: 12px; border-radius: 50%;
    background: var(--green);
    display: flex; align-items: center; justify-content: center;
  }
  .address {
    position: absolute; left: 34px; top: 162px;
    font-style: normal;
    font-size: 8px; letter-spacing: 1.5px; line-height: 1.8;
    text-transform: uppercase; color: var(--ink-soft);
  }
  .swoosh { position: absolute; left: 0; bottom: 0; width: 520px; height: 90px; }
  .swoosh-url {
    position: absolute; left: 250px; bottom: 12px;
    font-size: 8px; letter-spacing: 2px; color: #ffffff;
    white-space: nowrap;
    transform: rotate(-5deg); transform-origin: left bottom;
  }
</style>
</head>
<body>
<main class="stage">
  <section class="card card-front" aria-label="Card front">
    <div class="brand">
      <span class="brand-dot"></span>
      <span class="brand-name">Quiet Nudge</span>
    </div>
  </section>

  <section class="card card-back" aria-label="Card back">
    <div class="brand">
      <span class="brand-dot"></span>
      <span class="brand-name">Quiet Nudge</span>
    </div>

    <p class="holder">Dominic Pelling MRCVS</p>

    <ul class="contact-list">
      <li class="contact-item">
        <span class="contact-icon">
          <svg width="7" height="7" viewBox="0 0 10 10"><path d="M2 1l2 2-1 1.5c.8 1.5 1.5 2.2 3 3L7.5 6.5l2 2L8 10C4 9.5.5 6 0 2z" fill="#fff"/></svg>
        </span>07700 900418
      </li>
      <li class="contact-item">
        <span class="contact-icon">
          <svg width="7" height="7" viewBox="0 0 10 10"><rect x="0.5" y="2" width="9" height="6" fill="none" stroke="#fff"/><path d="M0.5 2l4.5 3.5L9.5 2" fill="none" stroke="#fff"/></svg>
        </span>dominic@quietnudge.co.uk
      </li>
      <li class="contact-item">
        <span class="contact-icon">
          <svg width="7" height="7" viewBox="0 0 10 10"><circle cx="5" cy="5" r="4.2" fill="none" stroke="#fff"/><path d="M1 5h8M5 1c-2 2.5-2 5.5 0 8M5 1c2 2.5 2 5.5 0 8" fill="none" stroke="#fff" stroke-width="0.8"/></svg>
        </span>www.quietnudge.co.uk
      </li>
    </ul>

    <address class="address">
      Oakmere Stanhurst<br>
      Lode Norwich NR14 2QJ
    </address>

    <svg class="swoosh" viewBox="0 0 520 90" preserveAspectRatio="none" aria-hidden="true">
      <defs>
        <linearGradient id="band" x1="0" y1="0" x2="1" y2="0">
          <stop offset="0" stop-color="#3f8a1c"/>
          <stop offset="1" stop-color="#8cc63f"/>
        </linearGradient>
      </defs>
      <path d="M0 78 C160 70 360 40 520 6 L520 90 L0 90 Z" fill="url(#band)"/>
      <path d="M0 70 C170 62 360 34 520 0" fill="none" stroke="#8cc63f" stroke-width="2"/>
    </svg>
    <span class="swoosh-url">www.quietnudge.co.uk</span>
  </section>
</main>
</body>
</html>
```